Medien Firma benötigt Briefpapier
Zielgruppe
Firma:
Wir sind im Bereich Veranstaltungstechnik und Eventmanagement seit 2007 tätig. Ab 2009 konnten wir unsere Expertise um die Bereiche Medientechnik und TV Produktion erweitern. Durch dieses Portfolio sind wir in der Lage, alle Facetten der technischen Planung durchzuführen.
Bereiche:
Veranstaltungstechnik - Medientechnik - Livestreaming
Kunden:
B2B
Aufgabenstellung
Erstellung von Briefpapier mit dem vorhandenen Logo.
Das Briefpapier soll auch als Produktsheet nutzbar sein. Also muss der Footer Text austauschbar sein.
Schlicht, Modern, Zeitlos, max. zwei Farben

```html
<!DOCTYPE html>
<html lang="de">
<head>
<meta charset="utf-8">
<title>nordwerk events – Briefpapier</title>
<link rel="stylesheet" href="https://fonts.googleapis.com/css2?family=Open+Sans:wght@400;700&display=swap">
<style>
  :root {
    --ink: #1a1a1a;
    --accent: #2aa3dc;
    --paper: #ffffff;
    --tile: #cccccc;
    --tile-light: #ececec;
  }
  * { margin: 0; padding: 0; box-sizing: border-box; }
  html, body {
    width: 848px;
    height: 1200px;
    overflow: hidden;
    background: var(--paper);
  }
  .letterhead {
    position: relative;
    width: 848px;
    height: 1200px;
    background: var(--paper);
    font-family: "Open Sans", Arial, sans-serif;
    color: var(--ink);
  }
  .brand {
    position: absolute;
    left: 50px;
    top: 50px;
    display: flex;
    align-items: center;
    gap: 14px;
  }
  .brand-square {
    width: 26px;
    height: 26px;
    background: var(--accent);
  }
  .brand-name {
    font-weight: 400;
    font-size: 34px;
    line-height: 1;
    color: var(--ink);
  }
  .sender {
    position: absolute;
    right: 52px;
    top: 46px;
    text-align: right;
    font-style: normal;
    font-size: 16px;
    line-height: 22px;
  }
  .sender-name { font-weight: 700; }
  .sender-web { font-weight: 700; color: var(--accent); }
  .bank-line {
    position: absolute;
    left: 50px;
    top: 1157px;
    font-size: 11px;
    color: var(--ink);
    white-space: nowrap;
    z-index: 1;
  }
  .bank-line .sep { margin: 0 16px; color: var(--ink); }
  .corner-pattern {
    position: absolute;
    right: 0;
    bottom: 0;
    width: 265px;
    height: 118px;
  }
</style>
</head>
<body>
  <main class="letterhead">
    <header>
      <div class="brand">
        <span class="brand-square"></span>
        <span class="brand-name">nordwerk events</span>
      </div>
      <address class="sender">
        <div class="sender-name">nordwerk events</div>
        <div>Lindenweg 42 / 50667 Köln</div>
        <div>+49 221 480 217 55 / info@nordwerk-events.de</div>
        <div class="sender-web">www.nordwerk-events.de</div>
      </address>
    </header>

    <footer>
      <svg class="corner-pattern" viewBox="0 0 265 118" role="img" aria-label="Dekoratives graues Kachelmuster, perspektivisch zur Ecke hin">
        <defs>
          <linearGradient id="cornerFade" x1="0" y1="1" x2="1" y2="0">
            <stop offset="0" stop-color="var(--tile-light)"/>
            <stop offset="1" stop-color="var(--tile)"/>
          </linearGradient>
        </defs>
        <path d="M0 118 L20 48 Q120 20 230 0 L265 30 L265 118 Z" fill="url(#cornerFade)"/>
      </svg>
      <p class="bank-line">Musterbank Köln<span class="sep">|</span>IBAN: DE00 0000 0000 0000 0000<span class="sep">|</span>BIC: MUSTER0000<span class="sep">|</span>UID: DE123456789</p>
    </footer>
  </main>
</body>
</html>
```